Custom Proposal

We need a custom proposal template created for our company. Our company, BRIGHTWAVE AUDIO SERVICES, provides in-store music and messaging services to businesses in the US and Canada. We need a 3-4 page document created that outlines our products and services that will accompany their proposal. The proposal needs to be created using company colors with a fresh feeling. Our music service is top quality and we service many major brands with customized music service. We have all of the copy and logos for partner companies. We need a designer to create a layout that will express our products and services in a fresh and exciting way.

Attached to this project you will find the following:

- PDF file title "Example". This is an example file of what we are looking for (minus the last page with the order fields).

- BRIGHTWAVE AUDIO SERVICES logo in EPS

- BRIGHTWAVE AUDIO SERVICES brand standards guideline

- Text copy for the flyer

- Styles (these match our web site)

- Font used on our web site and other material

- Zip file with logos of companies we do business with

We would also like a section that has the logos for these companies to showcase who we work with.

We prefer to have the project developed in an editable format such as Adobe Illustrator or PSD.

The paper size is 8 1/2" x 11" Portrait
Updates

Please note: We do NOT want the graphics included in the "Brands Standard Guide" that is attached to the project to be used for the project. The Brand Standards Guide is provided simply to show you how to use our logo, not to include the graphics used in the guide. Also, we do not want any computers or smart phones in the artwork. We provided the Pelican Harbor document as an example of one we liked, not to use the same graphics.

Please be sure to follow the outline of the project and use the images  supplied. Please also keep in mind we  are not looking for a template look  but rather  a  unique design  for each page that is themed for our industry. Our industry is in-store music and messaging services.

Thank you

Target Market(s)

Business owners, executives, marketing directors, business executives

Industry/Entity Type

Business

Requirements
Must have
• We are looking for fresh, open, personal, exciting, creative, and relevant designs.
Should not have
• We are NOT looking for stock template looking designs with no originality that look like a standard stock design.

```html
<!DOCTYPE html>
<html lang="en">
<head>
<meta charset="utf-8">
<title>Streaming Music for Business – BrightWave Audio Services</title>
<link href="https://fonts.googleapis.com/css2?family=Exo+2:wght@300;400;700;800&display=swap" rel="stylesheet">
<style>
  :root {
    --lime: #b9cc2e;
    --lime-deep: #a8bb22;
    --text-grey: #4a4a4a;
    --brand-grey: #6d6d6d;
    --paper: #ffffff;
    --paper-shade: #e6e6e6;
  }
  html, body {
    margin: 0;
    padding: 0;
    overflow: hidden;
  }
  body {
    width: 848px;
    height: 1200px;
  }
  .cover {
    position: relative;
    width: 848px;
    height: 1200px;
    overflow: hidden;
    background: linear-gradient(180deg, var(--paper) 0%, var(--paper) 72%, var(--paper-shade) 100%);
    font-family: "Exo 2", sans-serif;
  }
  .cover-shapes {
    position: absolute;
    inset: 0;
  }
  .brand {
    position: absolute;
    top: 72px;
    right: 36px;
    display: flex;
    align-items: center;
    gap: 16px;
  }
  .brand-mark {
    width: 46px;
    height: 46px;
    background: var(--lime);
  }
  .brand-name {
    font-weight: 400;
    font-size: 27px;
    letter-spacing: 1px;
    color: var(--brand-grey);
  }
  .headline {
    margin: 0;
    color: var(--paper);
    text-shadow: 0 2px 4px rgba(0, 0, 0, 0.25);
  }
  .headline span {
    position: absolute;
    left: 72px;
    line-height: 1;
    white-space: nowrap;
  }
  .headline-top {
    top: 712px;
    font-weight: 800;
    font-size: 80px;
    letter-spacing: 0.5px;
  }
  .headline-main {
    top: 772px;
    font-weight: 800;
    font-size: 136px;
  }
  .headline-bottom {
    top: 898px;
    font-weight: 300;
    font-size: 66px;
  }
  .intro {
    position: absolute;
    right: 20px;
    top: 1073px;
    width: 456px;
    margin: 0;
    text-align: right;
    font-size: 17px;
    line-height: 23.5px;
    color: var(--text-grey);
  }
  .intro strong {
    font-weight: 700;
  }
</style>
</head>
<body>
<main class="cover">
  <svg class="cover-shapes" width="848" height="1200" viewBox="0 0 848 1200">
    <defs>
      <radialGradient id="speaker-tone" cx="0.55" cy="0.45" r="0.8">
        <stop offset="0" stop-color="#4a4a4a"/>
        <stop offset="0.5" stop-color="#262626"/>
        <stop offset="1" stop-color="#0d0d0d"/>
      </radialGradient>
    </defs>
    <polygon class="speaker-photo" role="img" aria-label="Close-up photograph of a row of black studio speaker cones"
             points="0,0 324,0 848,360 848,840 0,492" fill="url(#speaker-tone)"/>
    <polygon class="lime-band" points="0,708 277,606 848,840 0,1152" fill="var(--lime)"/>
    <polygon class="lime-tint" points="277,606 848,396 848,840" fill="var(--lime-deep)" opacity="0.55"/>
  </svg>

  <div class="brand">
    <span class="brand-mark"></span>
    <span class="brand-name">BRIGHTWAVE AUDIO SERVICES</span>
  </div>

  <h1 class="headline">
    <span class="headline-top">STREAMING</span>
    <span class="headline-main">MUSIC</span>
    <span class="headline-bottom">FOR BUSINESS</span>
  </h1>

  <p class="intro">The leading provider of <strong>quality audio</strong>, video and messaging services for businesses throughout the US, dedicated to delivering unique and stress-free streaming solutions for our customers.</p>
</main>
</body>
</html>
```